BQN Project Signage

Need a sign to be displayed in the front of properties currently under Construction or Renovation to advertise our company information. Need it to be Professional and Contemporary. We are a Design/Build Construction Company. Information should include Company Name, email, website, phone number. Attached: Logo and company brochure, also included and inspiration images

```html
<!DOCTYPE html>
<html lang="en">
<head>
<meta charset="utf-8">
<title>BQN Construction – Project Sign</title>
<link rel="stylesheet" href="https://fonts.googleapis.com/css2?family=Playfair+Display:wght@400;500&display=swap">
<style>
  :root {
    --brand-yellow: #EDEA48;
    --ink-black: #060808;
    --paper-white: #FFFFFF;
    --serif: "Playfair Display", Georgia, serif;
  }
  html, body {
    margin: 0;
    padding: 0;
    width: 1200px;
    height: 1200px;
    overflow: hidden;
    background: var(--brand-yellow);
  }
  .canvas {
    position: relative;
    width: 1200px;
    height: 1200px;
  }
  .project-sign {
    position: absolute;
    left: 240px;
    top: 60px;
    width: 720px;
    height: 1080px;
    display: block;
  }
  .sign-text { font-family: var(--serif); }
  .fill-yellow { fill: var(--brand-yellow); }
  .fill-black { fill: var(--ink-black); }
  .fill-white { fill: var(--paper-white); }
</style>
</head>
<body>
<main class="canvas">
  <svg class="project-sign" viewBox="0 0 970 1455" role="img" aria-label="BQN Construction project sign">
    <!-- sign board -->
    <rect class="sign-board fill-white" x="0" y="0" width="970" height="1455"/>

    <!-- brand name -->
    <g class="brand-mark">
      <circle class="brand-dot fill-yellow" cx="270" cy="166" r="16"/>
      <text class="sign-text brand-name fill-black" x="300" y="182" font-size="46" font-weight="400">BQN Construction</text>
    </g>

    <!-- title band -->
    <rect class="title-band fill-black" x="0" y="369" width="970" height="388"/>
    <text class="sign-text title-initials fill-yellow" x="479" y="494" font-size="108" text-anchor="middle" textLength="200" lengthAdjust="spacingAndGlyphs">BQN</text>
    <text class="sign-text title-word fill-yellow" x="64" y="614" font-size="112" textLength="835" lengthAdjust="spacingAndGlyphs">CONSTRUCTION</text>
    <text class="sign-text title-tagline fill-white" x="204" y="687" font-size="30" textLength="575" lengthAdjust="spacing">LUXURY RENOVATIONS</text>

    <!-- email row -->
    <g class="contact-row contact-email">
      <rect class="contact-bar fill-yellow" x="139" y="863" width="692" height="97"/>
      <rect class="contact-icon-box fill-black" x="144" y="853" width="123" height="122"/>
      <g class="icon-mail" fill="none" stroke="var(--brand-yellow)" stroke-width="6" stroke-linejoin="round" stroke-linecap="round">
        <rect x="174" y="890" width="62" height="48" rx="5"/>
        <polyline points="180,898 205,916 230,898"/>
      </g>
      <text class="sign-text contact-text fill-black" x="331" y="922" font-size="40" textLength="452" lengthAdjust="spacingAndGlyphs">info@bqnbuildco.com</text>
    </g>

    <!-- website row -->
    <g class="contact-row contact-web">
      <rect class="contact-bar fill-yellow" x="139" y="1032" width="692" height="96"/>
      <rect class="contact-icon-box fill-black" x="144" y="1019" width="123" height="122"/>
      <g class="icon-web">
        <path d="M178 1068 A32 32 0 0 1 232 1068" fill="none" stroke="var(--brand-yellow)" stroke-width="9"/>
        <path d="M178 1092 A32 32 0 0 0 232 1092" fill="none" stroke="var(--brand-yellow)" stroke-width="9"/>
        <text class="fill-yellow" x="205" y="1088" font-family="Arial, sans-serif" font-weight="700" font-size="22" text-anchor="middle">www</text>
      </g>
      <text class="sign-text contact-text fill-black" x="331" y="1090" font-size="40" textLength="448" lengthAdjust="spacingAndGlyphs">www.bqnbuildco.com</text>
    </g>

    <!-- phone row -->
    <g class="contact-row contact-phone">
      <rect class="phone-bar fill-black" x="81" y="1249" width="808" height="115"/>
      <rect class="phone-icon-box fill-yellow" x="92" y="1238" width="124" height="137"/>
      <path class="icon-phone" transform="translate(116 1268) scale(3.3)" d="M22 16.92v3a2 2 0 0 1-2.18 2 19.79 19.79 0 0 1-8.63-3.07 19.5 19.5 0 0 1-6-6 19.79 19.79 0 0 1-3.07-8.67A2 2 0 0 1 4.11 2h3a2 2 0 0 1 2 1.72 12.84 12.84 0 0 0 .7 2.81 2 2 0 0 1-.45 2.11L8.09 9.91a16 16 0 0 0 6 6l1.270-1.27a2 2 0 0 1 2.110-.45 12.84 12.84 0 0 0 2.81.7A2 2 0 0 1 22 16.92z" fill="none" stroke="var(--ink-black)" stroke-width="1.8" stroke-linejoin="round" stroke-linecap="round"/>
      <text class="sign-text phone-number fill-yellow" x="325" y="1332" font-size="84" textLength="427" lengthAdjust="spacingAndGlyphs">555-014-2276</text>
    </g>
  </svg>
</main>
</body>
</html>
```